Flyer for American Indian Elders on Dementia Warning Signs

We need a flyer designed for older adults who are American Indian or Alaska Native (in the U.S.).

Ideally, the flyer should complement the colors of our logos. The project logo and our organization logo are attached to the brief.

When people see the flyer we want them to feel that it represents their culture, is warm, and professional but relatable to older adults and people who have limited incomes.

I have attached an earlier draft of the document we designed ourselves BUT we want different and better.

It is for older adults who have trouble reading so:
1. you must use a font that is 11.5 points or larger
2. Do not put text over complex pictures or use shading with words
3. You can use a serif font for the heading, but should use san serif for the body text
4. There should be good contrast between the font color and background

Please do not use any images that include a head dress or pictures of American Indian people or things that are very traditional or "token" imagery.

We need to save a small space under the call out box/ somewhere on the flyer for other people to add their logo once they download.

Let us know if you have questions or need additional information.

Target Market(s)

Older American Indian people

Font styles to use
Serif
Sans Serif

Requirements
Must have
• Easy to read for older adults
Should not have
• indian headdress

```html
<!DOCTYPE html>
<html lang="en">
<head>
<meta charset="utf-8">
<title>10 Signs of Thinking or Memory Changes That Might Be Dementia</title>
<link href="https://fonts.googleapis.com/css2?family=Oswald:wght@500;700&family=Arimo:ital,wght@0,400;0,700;1,400;1,700&display=swap" rel="stylesheet">
<style>
  :root {
    --red: #c21f32;
    --teal: #6aa9b4;
    --ink: #1f1f1f;
    --title-gray: #4a4a4a;
    --intro-gray: #555555;
    --sky: #e4eff1;
    --blush: #f8e5e7;
    --callout: #b3e0ea;
    --band: #e6e6e6;
    --white: #ffffff;
  }
  * { box-sizing: border-box; margin: 0; padding: 0; }
  html, body { width: 927px; height: 1200px; overflow: hidden; background: var(--white); }
  .flyer {
    position: relative; width: 927px; height: 1200px; overflow: hidden;
    font-family: "Arimo", Arial, sans-serif; color: var(--ink);
  }
  .backdrop, .path { position: absolute; left: 0; top: 0; }
  .abs { position: absolute; }

  .big-number {
    left: 38px; top: 30px; font-family: "Oswald", sans-serif; font-weight: 700;
    font-size: 180px; line-height: 1; color: var(--red); letter-spacing: -10px;
  }
  .headline {
    left: 200px; top: 58px; font-family: "Oswald", sans-serif; font-weight: 500;
    font-size: 42px; line-height: 50px; color: var(--title-gray); letter-spacing: -1.5px;
  }
  .headline .accent { color: var(--teal); }

  .intro {
    right: 52px; top: 60px; width: 262px; text-align: right;
    font-style: italic; font-size: 15.5px; line-height: 19.3px; color: var(--intro-gray);
  }
  .intro p + p { margin-top: 14px; }
  .intro .ask { color: var(--red); font-weight: 700; }
  .side-bar { right: 0; top: 48px; width: 15px; height: 278px; background: var(--red); }

  .step-num {
    width: 33px; height: 33px; border-radius: 50%; background: var(--red);
    border: 2px solid var(--white); color: var(--white); font-weight: 700;
    font-size: 20px; display: flex; align-items: center; justify-content: center;
  }
  .sign { font-size: 15.6px; line-height: 19.5px; }
  .sign h2 { font-size: 17px; line-height: 19.5px; font-weight: 700; }
  .sign .lead-in { font-size: 17px; }
  .sign ul { list-style: none; }
  .sign li::before { content: "• "; }

  .feather { border-radius: 50% 50% 50% 50% / 70% 70% 30% 30%; }

  .callout {
    left: 402px; top: 707px; width: 459px; height: 303px;
    background: var(--callout); border: 2px solid #333; border-radius: 14px;
    padding: 12px 34px 0 20px; font-size: 16px; line-height: 19.5px;
  }
  .callout li { list-style: none; position: relative; margin-bottom: 8px; }
  .callout li::before {
    content: ""; position: absolute; left: -24px; top: 5px; width: 9px; height: 9px;
    border-radius: 50%; background: var(--ink);
  }

  .logo-band { left: 0; top: 1022px; width: 927px; height: 76px; background: var(--band); }
  .logo-slot {
    left: 74px; top: 1030px; font-family: "Oswald", sans-serif; font-weight: 500;
    font-size: 40px; line-height: 58px; color: var(--white); letter-spacing: -1.5px;
  }
  .partner { display: flex; align-items: center; gap: 8px; font-weight: 700; }
  .partner .dot { width: 56px; height: 56px; border-radius: 50%; background: var(--teal); flex: none; }
  .partner-one { left: 402px; top: 1032px; width: 230px; font-size: 15px; line-height: 17px; color: var(--teal); }
  .partner-two { left: 660px; top: 1042px; width: 230px; font-size: 15px; line-height: 17px; color: var(--red); }

  .footer {
    left: 0; top: 1098px; width: 927px; height: 83px; background: var(--red);
    color: var(--white); text-align: center;
  }
  .footer .lead { font-style: italic; font-size: 16.5px; margin-top: 9px; }
  .footer .links { font-weight: 700; font-size: 30px; margin-top: 7px; }
</style>
</head>
<body>
<div class="flyer">
  <svg class="backdrop" width="927" height="1200" aria-hidden="true">
    <circle cx="250" cy="150" r="390" fill="var(--sky)"/>
    <circle cx="760" cy="820" r="400" fill="var(--blush)"/>
  </svg>

  <svg class="path" width="927" height="1200" aria-hidden="true" fill="none" stroke="var(--teal)" stroke-width="1.6">
    <path d="M72 250 V310 Q72 340 104 342 L384 350 L598 358 Q632 360 632 386 V534 Q632 540 596 538 L430 542 L186 552 L110 553 Q74 556 74 600 V906"/>
    <polyline points="216,341 222,345 216,349"/><polyline points="224,341 230,345 224,349"/><polyline points="232,341 238,345 232,349"/>
    <polyline points="486,350 492,354 486,358"/><polyline points="494,350 500,354 494,358"/><polyline points="502,350 508,354 502,358"/>
    <polyline points="312,542 306,546 312,550"/><polyline points="320,542 314,546 320,550"/><polyline points="328,542 322,546 328,550"/>
    <polyline points="70,790 74,796 78,790"/><polyline points="70,800 74,806 78,800"/><polyline points="70,810 74,816 78,810"/>
  </svg>

  <div class="abs big-number">10</div>
  <h1 class="abs headline">SIGNS OF THINKING OR<br>MEMORY CHANGES <span class="accent">THAT</span><br><span class="accent">MIGHT BE DEMENTIA</span></h1>

  <div class="abs intro">
    <p>As we get older, we may slow down a bit. This is a normal part of aging. <strong>Changes in memory or thinking that make it harder to get through the day,</strong> are not a normal part of aging. These may be <strong>early signs of dementia.</strong></p>
    <p>Because American Indian and Alaska Native people have a high risk of dementia, it is important to know the warning signs. <span class="ask">Do you have any of these 10 signs? If so, talk to your doctor.</span></p>
  </div>
  <div class="abs side-bar"></div>

  <div class="abs step-num" style="left:56px;top:222px">1</div>
  <div class="abs step-num" style="left:103px;top:326px">2</div>
  <div class="abs step-num" style="left:367px;top:334px">3</div>
  <div class="abs step-num" style="left:615px;top:369px">4</div>
  <div class="abs step-num" style="left:615px;top:447px">5</div>
  <div class="abs step-num" style="left:580px;top:518px">6</div>
  <div class="abs step-num" style="left:413px;top:526px">7</div>
  <div class="abs step-num" style="left:169px;top:536px">8</div>
  <div class="abs step-num" style="left:54px;top:713px">9</div>
  <div class="abs step-num" style="left:54px;top:890px">10</div>

  <section class="abs sign" style="left:114px;top:224px;width:470px">
    <h2>Memory loss that affects your daily life. You may:</h2>
    <ul><li>Forget events or important dates</li><li>Repeat yourself</li><li>Rely more often on lists or sticky notes to remember things</li></ul>
  </section>
  <section class="abs sign" style="left:67px;top:370px;width:205px">
    <h2>Trouble planning or solving problems. You may have a harder time:</h2>
    <ul><li>Paying bills</li><li>Cooking recipes you have used for years</li></ul>
  </section>
  <section class="abs sign" style="left:306px;top:384px;width:276px">
    <h2>Trouble with how your eyesight and thinking work together that gets worse. This includes:</h2>
    <ul><li>Tripping, falls, or problems with your balance</li><li>Spilling or dropping things more</li></ul>
  </section>
  <section class="abs sign" style="left:664px;top:368px;width:182px">
    <h2>Get confused about the time, date, or where you are.</h2>
  </section>
  <section class="abs sign" style="left:664px;top:446px;width:205px">
    <h2>Daily tasks are getting harder, including:</h2>
    <ul><li>Driving</li><li>Making a grocery list or going shopping</li></ul>
  </section>
  <section class="abs sign" style="left:597px;top:570px;width:262px">
    <h2>New trouble talking or writing.</h2>
    <p>You have a hard time finding the words you want to say. For example, you may say “that thing on your wrist that tells time” instead of “watch.”</p>
  </section>
  <section class="abs sign" style="left:368px;top:578px;width:200px">
    <p><b class="lead-in">Lose and cannot find things.</b> For example, you:</p>
    <ul><li>Can’t find the coffee pot that you use every day</li><li>Might put your car keys in the freezer</li></ul>
  </section>
  <section class="abs sign" style="left:98px;top:578px;width:235px">
    <h2>Notice changes in mood or personality, such as being:</h2>
    <ul><li>Easily mad or sad in everyday situations</li><li>More fearful (scared) or suspicious (not trusting)</li></ul>
  </section>
  <section class="abs sign" style="left:98px;top:712px;width:262px">
    <h2>Act different and make poor choices.</h2>
    <p>This may make you more likely to:</p>
    <ul><li>Spend money you do not have or be a scam victim</li><li>Stop washing up regularly or pay less attention to how you look</li><li>Forget to take care of your pet</li></ul>
  </section>
  <section class="abs sign" style="left:98px;top:892px;width:230px">
    <p><b class="lead-in">Pull away from friends and family because it is harder to keep up.</b> You may not want to do things you used to enjoy, like sporting events, church, music, or sex.</p>
  </section>

  <div class="abs feather" role="img" aria-label="Feather illustration, teal and red" style="left:24px;top:520px;width:62px;height:96px;background:linear-gradient(160deg,var(--teal),var(--red));"></div>
  <div class="abs feather" role="img" aria-label="Feather illustration, pale blue and red" style="left:836px;top:634px;width:68px;height:92px;background:linear-gradient(200deg,#b4cdd3,var(--red));"></div>

  <ul class="abs callout">
    <li>American Indian and Alaska Native elders have a higher risk of dementia &amp; younger Indian and Native people report more memory problems at a younger age.</li>
    <li>Big changes in memory, thinking, and ability that make it hard to get through the day are not a normal part of aging.</li>
    <li>People with one or more of these 10 warning signs should see their doctor to find the cause.</li>
    <li>Other health problems may also cause these same symptoms and may be treated.</li>
    <li><b>Early diagnosis gives you a chance to get care and plan for your future.</b></li>
  </ul>

  <div class="abs logo-band"></div>
  <div class="abs logo-slot">YOUR LOGO HERE</div>
  <div class="abs partner partner-one"><span class="dot"></span><span>Native Elders Brain Health Center</span></div>
  <div class="abs partner partner-two"><span>Council for Indigenous Aging Wellness</span></div>

  <footer class="abs footer">
    <p class="lead">To learn more about the warning signs of dementia in American Indian and Alaska Native people, visit:</p>
    <p class="links">www.ElderMindMatters.org &nbsp;|&nbsp; www.healthyagingnetwork.org</p>
  </footer>
</div>
</body>
</html>
```